Verpackungsdesign für Kaffeerösterei
Zielgruppe
wir Rösten Kaffee. Wir haben uns darauf Spezialisiert Hochwertigen Premium Caffe Crema herzustellen und bieten auch nur diesen in Unserem Shop www.korntal-bohne.de an. wir bieten 250gr. 500gr. Kaffee an. .
Es kann gerne verrückt oder anders sein, dennoch aber sehr edel.
die Zielgruppe ist weitgestreut, aber laut unserern Daten ist die Ideale Zielgruppe der 52 Jährige Mann, der Wert auf Hochwertige Genussmittel legt und auch bereit ist mehr Geld dafür zu bezahlen.
ich habe bereits ein beispiel design und die Druckvorlage bereitgestellt.
Aufgabenstellung
das Konzept unserer Internetseite sollte berücksichtigt werden, ansonsten ist dem Kreativen kopf keine Grenzen gesetzt.

```html
<!DOCTYPE html>
<html lang="de">
<head>
<meta charset="utf-8">
<title>Korntal Bohne – Café Crema Etikett</title>
<link href="https://fonts.googleapis.com/css2?family=Saira+Extra+Condensed:wght@300;600&display=swap" rel="stylesheet">
<style>
  :root {
    --stage: #737373;
    --paper: #ffffff;
    --gold: #e9c896;
    --bean-dark: #3b2417;
    --bean-mid: #7a4c2e;
    --bean-light: #a8734a;
  }
  * { box-sizing: border-box; margin: 0; padding: 0; }
  html, body { width: 1200px; height: 1200px; overflow: hidden; }
  body {
    background: var(--stage);
    font-family: "Saira Extra Condensed", "Arial Narrow", sans-serif;
    font-weight: 300;
    color: var(--gold);
    position: relative;
  }
  .label {
    position: absolute;
    top: 111px;
    width: 380px;
    height: 977px;
    background: var(--paper);
    overflow: hidden;
  }
  .label--front { left: 205px; }
  .label--back { left: 615px; }

  .brand {
    position: absolute;
    writing-mode: vertical-rl;
    transform: rotate(180deg);
    font-weight: 600;
    letter-spacing: 2px;
    white-space: nowrap;
    line-height: 1;
    text-align: center;
    overflow: hidden;
  }
  .label--front .brand { left: 138px; top: 39px; width: 106px; height: 354px; font-size: 50px; }
  .label--back .brand { left: 66px; top: 39px; width: 60px; height: 201px; font-size: 27px; }

  .weight {
    position: absolute;
    top: 412px;
    width: 100%;
    text-align: center;
    font-size: 22px;
    letter-spacing: 4px;
  }
  .beans-photo {
    position: absolute;
    left: 76px; top: 495px;
    width: 199px; height: 215px;
    border-radius: 45% 50% 48% 42%;
    background: radial-gradient(circle at 40% 40%, var(--bean-light), var(--bean-mid) 45%, var(--bean-dark) 80%, rgba(59,36,23,0) 100%);
  }
  .roast-stamp {
    position: absolute;
    left: 245px; top: 612px;
    width: 128px; height: 128px;
    border-radius: 50%;
    border: 1px solid var(--gold);
    background: rgba(233,200,150,0.18);
  }
  .product {
    position: absolute;
    top: 828px;
    width: 100%;
    text-align: center;
    font-size: 44px;
    font-weight: 300;
    letter-spacing: 4px;
    line-height: 1;
    white-space: nowrap;
  }
  .taste {
    position: absolute;
    top: 905px;
    width: 100%;
    text-align: center;
    font-size: 15px;
    letter-spacing: 2px;
    line-height: 26px;
    white-space: nowrap;
  }
  .web {
    position: absolute;
    top: 918px;
    width: 100%;
    text-align: center;
    font-size: 16px;
    letter-spacing: 2.5px;
    white-space: nowrap;
  }
  .facts {
    position: absolute;
    bottom: 235px;
    writing-mode: vertical-rl;
    transform: rotate(180deg);
    font-size: 15px;
    letter-spacing: 2px;
    line-height: 24px;
    white-space: nowrap;
  }
  .facts--origin { left: 54px; }
  .facts--roast { left: 162px; }
  .facts--taste { left: 269px; }
</style>
</head>
<body>
  <section class="label label--front">
    <div class="brand">KORNTAL<br>BOHNE</div>
    <p class="weight">500G</p>
    <div class="beans-photo" role="img" aria-label="Foto: drei geröstete Kaffeebohnen"></div>
    <div class="roast-stamp" role="img" aria-label="Stempel: handgeröstet"></div>
    <h1 class="product">CAFÉ CREMA</h1>
    <p class="taste">SCHOKOLADIG / LEICHT NUSSIG<br>SÄUREARM</p>
  </section>

  <section class="label label--back">
    <div class="brand">KORNTAL<br>BOHNE</div>
    <p class="facts facts--origin">70% ROBUSTA AUS INDIEN<br>30% HOCHLAND ARABICA AUS BRASILIEN</p>
    <p class="facts facts--roast">SCHONEND HANDGERÖSTET IM TROMMELRÖSTER<br>(CA. 22 MIN. BEI MAX. 255°C)</p>
    <p class="facts facts--taste">GESCHMACK:<br>SCHOKOLADIG / SÄUREARM / LEICHT NUSSIG</p>
    <h2 class="product">CAFÉ CREMA</h2>
    <p class="web">WWW.KORNTAL-BOHNE.DE</p>
  </section>
</body>
</html>
```